Salsa Company Needs New Label Design

Brookvale Food Company is company launching its second product line — La Tormenta Roja Salsa. We need a label that closely emulates the attached La Tormenta All-Natural Salsa label for layout inspiration and follows our existing color and brand guidelines as described in the attached Word document.

```html
<!DOCTYPE html>
<html lang="en">
<head>
<meta charset="utf-8">
<title>La Tormenta Roja Salsa – Label</title>
<link rel="stylesheet" href="https://fonts.googleapis.com/css2?family=Rye&family=Lobster&family=Oswald:wght@500&display=swap">
<style>
  :root {
    --page: #f4f1ec;
    --gold: #f2c230;
    --gold-light: #fbe27a;
    --crimson: #c8283a;
    --crimson-deep: #a81c2c;
    --flame-yellow: #f6e02a;
    --flame-orange: #f28a12;
    --flame-red: #e0321c;
    --panel: #d53a44;
    --panel-light: #e4525a;
    --cream: #fff6ea;
    --green: #2f7a2c;
    --ink: #2a1410;
  }
  * { box-sizing: border-box; margin: 0; padding: 0; }
  html, body { width: 1154px; height: 1200px; overflow: hidden; background: var(--page); }
  .canvas { position: relative; width: 1154px; height: 1200px; }

  .label {
    position: absolute; left: 40px; top: 60px; width: 1074px; height: 1080px;
    border-top: 22px solid var(--gold);
    border-bottom: 22px solid var(--gold);
    overflow: hidden;
  }
  .label::before, .label::after {
    content: ""; position: absolute; left: 0; right: 0; height: 8px; background: var(--crimson); z-index: 3;
  }
  .label::before { top: 10px; }
  .label::after { bottom: 10px; }

  .flame-field {
    position: absolute; inset: 0;
    background:
      radial-gradient(ellipse 55% 42% at 50% 32%, var(--flame-yellow) 0%, rgba(246,224,42,0) 70%),
      linear-gradient(180deg, var(--flame-orange) 0%, #ee6a14 45%, var(--flame-red) 100%);
  }

  .brand-name {
    position: absolute; left: 0; right: 0; top: 150px; text-align: center;
    font-family: "Rye", serif; font-size: 132px; line-height: 1; color: var(--crimson);
  }

  .product-panel {
    position: absolute; left: 187px; top: 470px; width: 700px; height: 370px;
    background: linear-gradient(160deg, var(--panel) 0%, var(--panel-light) 100%);
    border: 3px solid var(--crimson-deep);
    text-align: center;
  }
  .product-panel::before {
    content: ""; position: absolute; inset: 12px; border: 2px solid var(--gold-light); opacity: .8;
  }
  .product-name {
    position: relative; margin-top: 34px;
    font-family: "Lobster", cursive; font-size: 130px; line-height: 1;
    background: linear-gradient(180deg, var(--green) 0%, #8fbf7c 55%, var(--cream) 100%);
    -webkit-background-clip: text; background-clip: text; color: transparent;
  }
  .product-type {
    position: relative; display: flex; align-items: center; justify-content: center; gap: 22px;
    margin-top: 8px;
    font-family: "Rye", serif; font-size: 78px; line-height: 1; color: var(--cream);
  }
  .rule { display: block; width: 120px; height: 3px; background: var(--gold-light); position: relative; }
  .rule::after { content: ""; position: absolute; top: -5px; width: 12px; height: 12px; border-radius: 50%; background: var(--gold-light); }
  .rule--left::after { right: -6px; }
  .rule--right::after { left: -6px; }
  .tagline {
    position: relative; margin-top: 22px;
    font-family: "Oswald", sans-serif; font-weight: 500; font-size: 26px; letter-spacing: 1px; color: var(--cream);
  }

  .net-weight {
    position: absolute; left: 187px; top: 868px;
    font-family: "Oswald", sans-serif; font-weight: 500; font-size: 26px; color: var(--ink);
  }
  .heat-level {
    position: absolute; left: 0; right: 0; top: 905px; text-align: center;
    font-family: "Rye", serif; font-size: 84px; line-height: 1; color: var(--cream);
  }
</style>
</head>
<body>
  <main class="canvas">
    <section class="label">
      <div class="flame-field" role="img" aria-label="Flame pattern with gold speckles and sunburst rays in yellow, orange and red"></div>
      <h1 class="brand-name">La Tormenta</h1>
      <div class="product-panel">
        <h2 class="product-name">Roja</h2>
        <p class="product-type"><span class="rule rule--left"></span>SALSA<span class="rule rule--right"></span></p>
        <p class="tagline">AUTHENTIC FLAVOR | SMALL BATCH CRAFTED</p>
      </div>
      <p class="net-weight">NET WT 16OZ (454g)</p>
      <p class="heat-level">HOT</p>
    </section>
  </main>
</body>
</html>
```